Email Banner Ad for Tidewell Power company

We are looking for an Email Banner Ad for all emails which is link to website

Regarding MEES compliance coming in April 2018

All the details can be found on our website www.brindlequay.co.uk

Our current footer is attached from last year and we are looking for a new one

Target Market(s)

Property companies and investor

Industry/Entity Type

It Company

Requirements
Must have
• a link to website
• must be the size to go at the bottom of emails
Nice to have
• similar to website
• similar to the advertisement we have had done already

```html
<!DOCTYPE html>
<html lang="en">
<head>
<meta charset="utf-8">
<title>Tidewell Power – MEES Compliance email banners</title>
<link href="https://fonts.googleapis.com/css2?family=Roboto:ital,wght@0,300;0,400;0,700;1,300;1,400&display=swap" rel="stylesheet">
<style>
:root{
  --page:#ffffff;
  --panel:#f2f2f2;
  --panel-white:#ffffff;
  --rule:#cfcfcf;
  --ink:#333333;
  --ink-soft:#555555;
  --green:#00b336;
  --sky:#00c4f5;
  --night-top:#0b1a7a;
  --night-mid:#2446d8;
  --night-low:#07104f;
  --teal-top:#0b7fa0;
  --teal-mid:#3fd9e8;
  --teal-low:#06384a;
  --white:#ffffff;
}
*{margin:0;padding:0;box-sizing:border-box}
html,body{width:768px;height:1200px;overflow:hidden;background:var(--page)}
body{position:relative;font-family:"Roboto",Arial,sans-serif;color:var(--ink)}

.banner{position:absolute;left:63px;width:643px;height:79px;background:var(--panel);overflow:hidden;--accent:var(--green);--shift:0px}
.banner--outlined{background:var(--panel-white);border:1px solid var(--rule)}
.banner--sky{--accent:var(--sky)}
.banner--wide{--shift:70px}

.banner__headline{position:absolute;top:14px;text-align:center;line-height:1}
.banner__title{display:block;font-size:22px;font-weight:700;letter-spacing:.1px;color:var(--ink)}
.banner__date{display:block;margin-top:4px;font-size:15px;font-style:italic;font-weight:400;letter-spacing:.3px;color:var(--ink)}
.banner--light .banner__title{font-weight:300}
.banner--light .banner__date{font-weight:300;color:var(--ink-soft)}

.banner--cta .banner__headline{left:16px;width:206px;top:23px}
.banner--news .banner__headline{left:64px;width:244px;top:23px}
.banner--cta.banner--wide .banner__headline{left:48px;width:206px}
.banner--news.banner--wide .banner__headline{left:100px;width:244px}

.banner__accent{position:absolute;inset:0;background:var(--accent)}
.banner--cta .banner__accent{clip-path:polygon(calc(253px + var(--shift)) 0,calc(333px + var(--shift)) 0,calc(309px + var(--shift)) 100%,calc(228px + var(--shift)) 100%)}
.banner--news .banner__accent{clip-path:polygon(calc(330px + var(--shift)) 0,calc(335px + var(--shift)) 5px,calc(311px + var(--shift)) 100%,calc(305px + var(--shift)) 100%)}

.banner__cta{position:absolute;top:37px;left:calc(250px + var(--shift));font-size:8px;font-weight:700;color:var(--white);text-decoration:none;letter-spacing:-.1px;line-height:1}

.banner__photo{position:absolute;inset:0;background:linear-gradient(180deg,var(--night-top) 0%,var(--night-mid) 55%,var(--night-low) 100%)}
.banner__photo--teal{background:linear-gradient(180deg,var(--teal-top) 0%,var(--teal-mid) 55%,var(--teal-low) 100%)}
.banner--cta .banner__photo{clip-path:polygon(calc(333px + var(--shift)) 0,100% 0,100% 100%,calc(309px + var(--shift)) 100%)}
.banner--news .banner__photo{clip-path:polygon(calc(336px + var(--shift)) 6px,100% 6px,100% 100%,calc(312px + var(--shift)) 100%)}

.news-ribbon{position:absolute;left:12px;top:0;width:50px;height:67px}
.news-ribbon__label{font-family:"Roboto",Arial,sans-serif;font-size:8.5px;font-weight:400;fill:var(--white)}
</style>
</head>
<body>

<!-- 1 -->
<div class="banner banner--cta" style="top:63px">
  <div class="banner__headline"><span class="banner__title">MEES COMPLIANCE</span><span class="banner__date">coming in April 2018</span></div>
  <div class="banner__accent"></div>
  <a class="banner__cta" href="http://www.brindlequay.co.uk">LEARN MORE »</a>
  <div class="banner__photo" role="img" aria-label="Night photograph of a lit suspension bridge over a river"></div>
</div>

<!-- 2 -->
<div class="banner banner--news" style="top:174px">
  <svg class="news-ribbon" viewBox="0 0 50 67" aria-hidden="true">
    <polygon points="0,0 50,0 50,67 25,59 0,67" fill="var(--green)"/>
    <g fill="none" stroke="var(--white)" stroke-width="2.4" stroke-linejoin="round">
      <path d="M12 18 L12 34 Q18 31 25 35 Q32 31 38 34 L38 18 Q32 15 25 19 Q18 15 12 18 Z"/>
      <line x1="25" y1="19" x2="25" y2="35"/>
    </g>
    <circle cx="25" cy="11" r="3.4" fill="var(--white)"/>
    <text class="news-ribbon__label" x="25" y="48" text-anchor="middle">NEWS</text>
  </svg>
  <div class="banner__headline"><span class="banner__title">MEES COMPLIANCE</span><span class="banner__date">coming in April 2018</span></div>
  <div class="banner__accent"></div>
  <div class="banner__photo" role="img" aria-label="Night photograph of a lit suspension bridge over a river"></div>
</div>

<!-- 3 -->
<div class="banner banner--cta banner--outlined" style="top:284px">
  <div class="banner__headline"><span class="banner__title">MEES COMPLIANCE</span><span class="banner__date">coming in April 2018</span></div>
  <div class="banner__accent"></div>
  <a class="banner__cta" href="http://www.brindlequay.co.uk">LEARN MORE »</a>
  <div class="banner__photo" role="img" aria-label="Night photograph of a lit suspension bridge over a river"></div>
</div>

<!-- 4 -->
<div class="banner banner--news banner--outlined" style="top:395px">
  <svg class="news-ribbon" viewBox="0 0 50 67" aria-hidden="true">
    <polygon points="0,0 50,0 50,67 25,59 0,67" fill="var(--green)"/>
    <g fill="none" stroke="var(--white)" stroke-width="2.4" stroke-linejoin="round">
      <path d="M12 18 L12 34 Q18 31 25 35 Q32 31 38 34 L38 18 Q32 15 25 19 Q18 15 12 18 Z"/>
      <line x1="25" y1="19" x2="25" y2="35"/>
    </g>
    <circle cx="25" cy="11" r="3.4" fill="var(--white)"/>
    <text class="news-ribbon__label" x="25" y="48" text-anchor="middle">NEWS</text>
  </svg>
  <div class="banner__headline"><span class="banner__title">MEES COMPLIANCE</span><span class="banner__date">coming in April 2018</span></div>
  <div class="banner__accent"></div>
  <div class="banner__photo" role="img" aria-label="Night photograph of a lit suspension bridge over a river"></div>
</div>

<!-- 5 -->
<div class="banner banner--cta banner--outlined banner--light banner--sky" style="top:506px">
  <div class="banner__headline"><span class="banner__title">MEES COMPLIANCE</span><span class="banner__date">coming in April 2018</span></div>
  <div class="banner__accent"></div>
  <a class="banner__cta" href="http://www.brindlequay.co.uk">LEARN MORE »</a>
  <div class="banner__photo" role="img" aria-label="Night photograph of a lit suspension bridge over a river"></div>
</div>

<!-- 6 -->
<div class="banner banner--news banner--outlined banner--light banner--sky" style="top:616px">
  <svg class="news-ribbon" viewBox="0 0 50 67" aria-hidden="true">
    <polygon points="0,0 50,0 50,67 25,59 0,67" fill="var(--green)"/>
    <g fill="none" stroke="var(--white)" stroke-width="2.4" stroke-linejoin="round">
      <path d="M12 18 L12 34 Q18 31 25 35 Q32 31 38 34 L38 18 Q32 15 25 19 Q18 15 12 18 Z"/>
      <line x1="25" y1="19" x2="25" y2="35"/>
    </g>
    <circle cx="25" cy="11" r="3.4" fill="var(--white)"/>
    <text class="news-ribbon__label" x="25" y="48" text-anchor="middle">NEWS</text>
  </svg>
  <div class="banner__headline"><span class="banner__title">MEES COMPLIANCE</span><span class="banner__date">coming in April 2018</span></div>
  <div class="banner__accent"></div>
  <div class="banner__photo" role="img" aria-label="Night photograph of a lit suspension bridge over a river"></div>
</div>

<!-- 7 -->
<div class="banner banner--cta banner--outlined banner--light banner--sky" style="top:726px">
  <div class="banner__headline"><span class="banner__title">MEES COMPLIANCE</span><span class="banner__date">coming in April 2018</span></div>
  <div class="banner__accent"></div>
  <a class="banner__cta" href="http://www.brindlequay.co.uk">LEARN MORE »</a>
  <div class="banner__photo banner__photo--teal" role="img" aria-label="Teal-toned night photograph of a lit suspension bridge over a river"></div>
</div>

<!-- 8 -->
<div class="banner banner--news banner--outlined banner--light banner--sky" style="top:838px">
  <svg class="news-ribbon" viewBox="0 0 50 67" aria-hidden="true">
    <polygon points="0,0 50,0 50,67 25,59 0,67" fill="var(--green)"/>
    <g fill="none" stroke="var(--white)" stroke-width="2.4" stroke-linejoin="round">
      <path d="M12 18 L12 34 Q18 31 25 35 Q32 31 38 34 L38 18 Q32 15 25 19 Q18 15 12 18 Z"/>
      <line x1="25" y1="19" x2="25" y2="35"/>
    </g>
    <circle cx="25" cy="11" r="3.4" fill="var(--white)"/>
    <text class="news-ribbon__label" x="25" y="48" text-anchor="middle">NEWS</text>
  </svg>
  <div class="banner__headline"><span class="banner__title">MEES COMPLIANCE</span><span class="banner__date">coming in April 2018</span></div>
  <div class="banner__accent"></div>
  <div class="banner__photo banner__photo--teal" role="img" aria-label="Teal-toned night photograph of a lit suspension bridge over a river"></div>
</div>

<!-- 9 -->
<div class="banner banner--cta banner--wide" style="top:948px">
  <div class="banner__headline"><span class="banner__title">MEES COMPLIANCE</span><span class="banner__date">coming in April 2018</span></div>
  <div class="banner__accent"></div>
  <a class="banner__cta" href="http://www.brindlequay.co.uk">LEARN MORE »</a>
  <div class="banner__photo" role="img" aria-label="Night photograph of a lit suspension bridge over a river"></div>
</div>

<!-- 10 -->
<div class="banner banner--news banner--wide" style="top:1058px">
  <svg class="news-ribbon" viewBox="0 0 50 67" aria-hidden="true">
    <polygon points="0,0 50,0 50,67 25,59 0,67" fill="var(--green)"/>
    <g fill="none" stroke="var(--white)" stroke-width="2.4" stroke-linejoin="round">
      <path d="M12 18 L12 34 Q18 31 25 35 Q32 31 38 34 L38 18 Q32 15 25 19 Q18 15 12 18 Z"/>
      <line x1="25" y1="19" x2="25" y2="35"/>
    </g>
    <circle cx="25" cy="11" r="3.4" fill="var(--white)"/>
    <text class="news-ribbon__label" x="25" y="48" text-anchor="middle">NEWS</text>
  </svg>
  <div class="banner__headline"><span class="banner__title">MEES COMPLIANCE</span><span class="banner__date">coming in April 2018</span></div>
  <div class="banner__accent"></div>
  <div class="banner__photo" role="img" aria-label="Night photograph of a lit suspension bridge over a river"></div>
</div>

</body>
</html>
```